Interactive Banner for Brookhaven Elementary School

title :"A Season of Bright Sparks”
Slogan: Khao, Khelo, Badho
(Eat, Play, Grow)

Students will place pictures of themselves doing their favorite sport or physical activity so will need space for 200 students.

Banner is around 128 sq feet. Will get exact dimensions.

Banner dimensions Length: 14 ft 9 in Height: 6 ft 9in

The border can be international flags, athletic symbols, etc..

Maybe use watermark athletic symbols in the background

incorporate logo

Target Market(s)

School community and mostly students to bring awareness to a healthy lifestyle

Industry/Entity Type

School

Font styles to use
Serif
Sans Serif

Requirements
Must have
• Space for photograph of children
• "A Season of Bright Sparks”
• Khao, Khelo, Badho
• (Eat, Play, Grow)
• Use our color palate listed. see below.
Nice to have
• international flag border

```html
<!DOCTYPE html>
<html lang="en">
<head>
<meta charset="utf-8">
<title>A Season of Bright Sparks – Brookhaven Elementary School</title>
<link rel="stylesheet" href="https://fonts.googleapis.com/css2?family=Roboto+Condensed:wght@700;800&display=swap">
<style>
  :root {
    --paper: #ffffff;
    --frame-line: #b9b9b9;
    --school-green: #13472f;
    --ink: #2a2a2a;
    --slot-gold: #c9b57c;
    --flag-red: #c8262d;
    --flag-green: #3e8a4a;
    --flag-blue: #1f3f8f;
    --flag-yellow: #f0c531;
    --flag-orange: #e98a2b;
  }
  html, body {
    margin: 0;
    padding: 0;
    overflow: hidden;
    background: var(--paper);
  }
  .banner {
    position: relative;
    width: 1200px;
    height: 578px;
    background: var(--paper);
    overflow: hidden;
    font-family: "Roboto Condensed", "Arial Narrow", sans-serif;
    font-weight: 700;
  }
  .banner__outline {
    position: absolute;
    left: 20px; top: 20px;
    width: 1158px; height: 536px;
    border: 1px solid var(--frame-line);
  }
  .flag-band {
    position: absolute;
    background: linear-gradient(90deg,
      var(--flag-red) 0%, var(--flag-green) 14%, var(--flag-blue) 28%,
      var(--flag-yellow) 42%, var(--flag-red) 56%, var(--flag-green) 70%,
      var(--flag-blue) 84%, var(--flag-red) 100%);
  }
  .flag-band--top    { left: 21px; top: 21px;  width: 1157px; height: 22px; }
  .flag-band--bottom { left: 21px; top: 534px; width: 1157px; height: 22px; }
  .flag-band--left, .flag-band--right {
    top: 43px; width: 22px; height: 491px;
    background: linear-gradient(180deg,
      var(--flag-blue) 0%, var(--flag-red) 15%, var(--flag-green) 30%,
      var(--flag-orange) 45%, var(--flag-yellow) 60%, var(--flag-green) 75%,
      var(--flag-red) 100%);
  }
  .flag-band--left  { left: 21px; }
  .flag-band--right { left: 1156px; }

  .school-name {
    position: absolute;
    left: 56px; top: 70px;
    width: 120px;
    margin: 0;
    display: flex;
    flex-direction: column;
    align-items: center;
    gap: 8px;
    text-align: center;
    color: var(--school-green);
    font-size: 15px;
    font-weight: 700;
    line-height: 1.15;
    text-transform: uppercase;
  }
  .school-name__mark {
    width: 34px; height: 34px;
    border-radius: 50%;
    border: 2px solid var(--slot-gold);
  }

  .headline {
    position: absolute;
    left: 186px; top: 52px;
    width: 960px;
    margin: 0;
    text-align: center;
    color: var(--school-green);
    font-size: 72px;
    font-weight: 800;
    line-height: 1;
    letter-spacing: 0.5px;
    text-transform: uppercase;
  }
  .slogan {
    position: absolute;
    left: 186px; top: 132px;
    width: 960px;
    margin: 0;
    text-align: center;
    color: var(--ink);
    font-size: 36px;
    font-weight: 700;
    line-height: 1;
    letter-spacing: 1px;
    text-transform: uppercase;
  }
  .slogan-translation {
    position: absolute;
    left: 186px; top: 172px;
    width: 960px;
    margin: 0;
    text-align: center;
    color: var(--ink);
    font-size: 15px;
    font-weight: 700;
    line-height: 1;
    letter-spacing: 0.5px;
  }

  .photo-wall {
    position: absolute;
    left: 54px; top: 198px;
  }
</style>
</head>
<body>
<main class="banner">
  <div class="banner__outline"></div>
  <div class="flag-band flag-band--top" role="img" aria-label="Border of international flags"></div>
  <div class="flag-band flag-band--bottom" role="img" aria-label="Border of international flags"></div>
  <div class="flag-band flag-band--left" role="img" aria-label="Border of international flags"></div>
  <div class="flag-band flag-band--right" role="img" aria-label="Border of international flags"></div>

  <p class="school-name"><span class="school-name__mark"></span>Brookhaven Elementary School</p>

  <h1 class="headline">A Season of Bright Sparks</h1>
  <p class="slogan">Khao, Khelo, Badho…</p>
  <p class="slogan-translation">(Eat, Play, Grow)</p>

  <svg class="photo-wall" width="1092" height="330" viewBox="0 0 1092 330" aria-label="Spaces for 200 student photos">
    <defs>
      <rect id="photo-slot" width="36" height="36" fill="none" stroke="#c9b57c" stroke-width="0.8"/>
      <g id="slot-row">
        <use href="#photo-slot" x="0"/><use href="#photo-slot" x="44"/><use href="#photo-slot" x="88"/>
        <use href="#photo-slot" x="132"/><use href="#photo-slot" x="176"/><use href="#photo-slot" x="220"/>
        <use href="#photo-slot" x="264"/><use href="#photo-slot" x="308"/><use href="#photo-slot" x="352"/>
        <use href="#photo-slot" x="396"/><use href="#photo-slot" x="440"/><use href="#photo-slot" x="484"/>
        <use href="#photo-slot" x="528"/><use href="#photo-slot" x="572"/><use href="#photo-slot" x="616"/>
        <use href="#photo-slot" x="660"/><use href="#photo-slot" x="704"/><use href="#photo-slot" x="748"/>
        <use href="#photo-slot" x="792"/><use href="#photo-slot" x="836"/><use href="#photo-slot" x="880"/>
        <use href="#photo-slot" x="924"/><use href="#photo-slot" x="968"/><use href="#photo-slot" x="1012"/>
        <use href="#photo-slot" x="1056"/>
      </g>
    </defs>
    <use href="#slot-row" y="0.5"/>
    <use href="#slot-row" y="42.5"/>
    <use href="#slot-row" y="84.5"/>
    <use href="#slot-row" y="126.5"/>
    <use href="#slot-row" y="168.5"/>
    <use href="#slot-row" y="210.5"/>
    <use href="#slot-row" y="252.5"/>
    <use href="#slot-row" y="293.5"/>
  </svg>
</main>
</body>
</html>
```